Letterhead in Word Format

We are a small law firm in the Midwest. Our clientele is generally small business owners and companies.

We recently had a complete re-brand with a new logo, new letterhead, business cards, etc. However, the major issue now is that we cannot use the letterhead without physically ordering letterhead. Thus, invoices, and other items cannot be custom drafted.

We require custom letterhead in MICROSOFT WORD format. Our logo will be provided to you. And we will also provide a copy of the letterhead that was prepared.

We would like to see designs that are black and white, sophisticated, elegant, and generally professional. We prefer a traditional design with just a touch of contemporary.

Please do not submit any designs that are not Microsoft Word compatible.

EDIT: Please view the attached letterhead. The design must include the logo, name, address, fax, phone, email, and name of attorney.
Updates

Thank you all for submitting designs. I just wanted to quickly provide some feedback. I saw a few designs that had the logo at the bottom. Because there will be text with margins at 1" all around, it's not practical have the logo at the bottom. Also, designs with blocks of gray or black would cause our printer to bleed black onto the letterhead, so that is not practical as well.

If you have any comments, please feel free to leave me a message. Thank you.

Target Market(s)

Small business owners, companies, real estate investors and developers.

Industry/Entity Type

Small Business

Font styles to use
Script

Requirements
Must have
• Microsoft Word Format

```html
<!DOCTYPE html>
<html lang="en">
<head>
<meta charset="utf-8">
<title>The RMB Law Firm — Letterhead</title>
<link rel="stylesheet" href="https://fonts.googleapis.com/css2?family=Cormorant+Garamond:wght@500;600&display=swap">
<style>
  :root {
    --paper: #ffffff;
    --ink: #2b2b2b;
    --mark-tint: #ececec;
  }
  * { margin: 0; padding: 0; box-sizing: border-box; }
  html, body {
    width: 900px;
    height: 1200px;
    overflow: hidden;
    background: var(--paper);
  }
  .letterhead {
    position: relative;
    width: 900px;
    height: 1200px;
    background: var(--paper);
    color: var(--ink);
    font-family: "Cormorant Garamond", Georgia, serif;
  }
  .masthead {
    position: absolute;
    top: 60px;
    left: 0;
    width: 100%;
    height: 160px;
  }
  .masthead-mark {
    position: absolute;
    left: 50%;
    top: 0;
    transform: translateX(-50%);
  }
  .firm-name {
    position: absolute;
    top: 62px;
    width: 100%;
    text-align: center;
    font-weight: 600;
    font-size: 24px;
    letter-spacing: 1.5px;
  }
  .contact-footer {
    position: absolute;
    bottom: 14px;
    width: 100%;
    text-align: center;
    font-weight: 500;
    font-size: 14px;
    line-height: 22px;
    letter-spacing: 0.6px;
    text-transform: uppercase;
  }
</style>
</head>
<body>
  <div class="letterhead">
    <header class="masthead">
      <svg class="masthead-mark" width="160" height="160" viewBox="0 0 160 160" aria-hidden="true">
        <circle cx="80" cy="80" r="70" fill="none" stroke="var(--mark-tint)" stroke-width="2"/>
      </svg>
      <h1 class="firm-name">THE RMB LAW FIRM</h1>
    </header>

    <footer class="contact-footer">
      <p class="address">2840 N. Harlan Ave. Oak Ridge, IL 60199 USA</p>
      <p class="contact-line">Phone : (555) 410-2280 | Fax : (555) 410-2281 | Email : info@thermblawfirm.com</p>
    </footer>
  </div>
</body>
</html>
```